The Bayfield Wellness Clinic - Practice Flyer

We need a flyer that generally advertises our services. I've uploaded one old flyer as well as examples of others. I like the style of the materials made by this practice: https://www.facebook.com/PineRidgeCounselingHouse

```html
<!DOCTYPE html>
<html lang="en">
<head>
<meta charset="utf-8">
<title>The Bayfield Wellness Clinic – Practice Flyer</title>
<link rel="stylesheet" href="https://fonts.googleapis.com/css2?family=Cinzel:wght@500;600&family=Crimson+Text&family=Open+Sans:wght@400;600;700&display=swap">
<style>
  :root {
    --olive: #8a8f5a;
    --olive-dark: #5f6337;
    --leaf: #bccb82;
    --cream: #f3f1e2;
    --ink: #2b2b22;
    --rust: #c5834a;
    --honey: rgba(246, 214, 138, 0.88);
    --mist: #e3e2da;
    --page: #eeece6;
  }
  * { box-sizing: border-box; margin: 0; padding: 0; }
  html, body { width: 1200px; height: 1200px; overflow: hidden; background: var(--page); }
  body { font-family: "Open Sans", sans-serif; color: var(--ink); }

  .flyer {
    position: absolute; left: 204px; top: 40px; width: 792px; height: 1120px;
    background: #fff; overflow: hidden; box-shadow: 0 4px 18px rgba(0,0,0,0.18);
  }
  .abs { position: absolute; }

  /* Header */
  .brand { left: 30px; top: 18px; width: 420px; text-align: center; }
  .brand-name {
    font-family: "Cinzel", serif; font-weight: 600; color: var(--olive-dark);
    font-size: 34px; line-height: 1.12; letter-spacing: 1px;
  }
  .brand-tag {
    font-family: "Cinzel", serif; font-weight: 500; color: var(--ink);
    font-size: 12px; letter-spacing: 1px; margin-top: 4px;
  }
  .phone {
    left: 496px; top: 72px; width: 296px; height: 44px; background: var(--mist);
    border-radius: 22px 0 0 22px; display: flex; align-items: center;
  }
  .phone-icon {
    width: 36px; height: 36px; margin-left: 4px; border-radius: 50%;
    background: var(--olive); display: flex; align-items: center; justify-content: center;
  }
  .phone-number { font-family: "Crimson Text", serif; font-size: 30px; color: var(--ink); margin-left: 18px; }

  /* Top photo + band */
  .photo-wall {
    left: 0; top: 133px; width: 792px; height: 350px;
    background: linear-gradient(100deg, #9a9787 0%, #b3ae9c 30%, #8f8a7a 55%, #6d665a 75%, #8b8676 100%);
  }
  .band { left: 0; top: 440px; width: 792px; height: 160px; }
  .about {
    left: 88px; top: 166px; width: 280px; height: 331px; background: var(--leaf);
    text-align: center; padding: 38px 16px 0;
  }
  .about-tab {
    left: 142px; top: 150px; width: 172px; height: 36px; background: var(--olive);
    color: var(--cream); font-family: "Cinzel", serif; font-weight: 500; font-size: 21px;
    text-transform: uppercase; text-align: center; line-height: 36px; letter-spacing: 1px;
  }
  .about-lead { font-weight: 700; font-size: 13px; line-height: 19.5px; }
  .about-rule { display: block; margin: 6px auto 12px; width: 180px; height: 12px; }
  .about-body { font-size: 14px; line-height: 21px; }
  .disorders {
    left: 20px; top: 506px; width: 752px; text-align: center; color: var(--cream);
    font-size: 14px; line-height: 21px;
  }

  /* Lower */
  .photo-sunset {
    left: 0; top: 595px; width: 792px; height: 525px;
    background: radial-gradient(ellipse at 85% 8%, #fbf5e6 0%, #f7e6bf 28%, transparent 55%),
                linear-gradient(160deg, #f4dca6 0%, #efb45c 40%, #d87b2a 70%, #a9521f 100%);
  }
  .cbt-note { left: 367px; top: 607px; width: 400px; text-align: center; font-size: 14.5px; line-height: 21px; }
  .treatments { left: 390px; top: 699px; width: 367px; height: 278px; background: var(--honey); }
  .treatments-title {
    left: 379px; top: 711px; width: 385px; height: 46px; background: var(--rust);
    color: #fff4e4; font-family: "Cinzel", serif; font-weight: 500; font-size: 22px;
    text-transform: uppercase; text-align: center; line-height: 42px;
    letter-spacing: 1px; border: 2px solid #e5b57f; outline: 3px solid var(--rust);
  }
  .treatment-list { left: 390px; top: 787px; width: 367px; list-style: none; text-align: center; font-size: 14.5px; line-height: 21px; }
  .footer-curve { left: 0; top: 1010px; width: 792px; height: 110px; }
  .director {
    left: 362px; top: 980px; width: 414px; height: 83px; background: var(--olive);
    color: var(--cream); text-align: center; padding-top: 11px;
  }
  .director-name { font-size: 14.5px; line-height: 1.35; }
  .director-lic { font-size: 11px; margin-top: 6px; }
  .social { left: 80px; top: 1060px; display: flex; gap: 16px; }
  .social span { width: 46px; height: 46px; border-radius: 50%; border: 3px solid #fff; box-shadow: 0 0 0 2px var(--c); background: var(--c); }
  .website { left: 342px; top: 1074px; width: 427px; text-align: right; font-size: 20px; color: var(--ink); }
</style>
</head>
<body>
<main class="flyer">
  <header>
    <div class="abs brand">
      <div class="brand-name">The Bayfield<br>Wellness Clinic</div>
      <div class="brand-tag">of Greater Bayfield LLC</div>
    </div>
    <div class="abs phone">
      <span class="phone-icon">
        <svg width="18" height="18" viewBox="0 0 24 24"><path fill="#fff" d="M6.6 10.8a15.1 15.1 0 0 0 6.6 6.6l2.2-2.2c.3-.3.7-.4 1-.2 1.1.4 2.3.6 3.6.6.6 0 1 .4 1 1V20c0 .6-.4 1-1 1A17 17 0 0 1 3 4c0-.6.4-1 1-1h3.5c.6 0 1 .4 1 1 0 1.3.2 2.5.6 3.6.1.3 0 .7-.2 1z"/></svg>
      </span>
      <span class="phone-number">(555) 014-2287</span>
    </div>
  </header>

  <section class="about-section">
    <div class="abs photo-wall" role="img" aria-label="Photo of a young person in a hooded sweater sitting slumped in front of an old wooden door and stone wall"></div>
    <svg class="abs band" viewBox="0 0 792 160" preserveAspectRatio="none"><path d="M0 28 Q 300 -8 792 10 L792 160 L0 160 Z" fill="var(--olive)"/></svg>
    <div class="abs about">
      <p class="about-lead">The Bayfield Wellness Clinic of Greater Bayfield (BWC) provides expert clinical care for anxiety disorders, obsessive compulsive and related disorders &amp; neurodevelopmental disorders in children, adolescents &amp; adults.</p>
      <svg class="about-rule" viewBox="0 0 180 12"><line x1="0" y1="8" x2="180" y2="8" stroke="var(--ink)" stroke-width="1"/><path d="M86 1 L90 7 L94 1" fill="none" stroke="var(--ink)" stroke-width="1.5"/></svg>
      <p class="about-body">BWC proudly provides the Greater Bayfield community with state-of-the-art assessment and evidence-based therapy for disorders including:</p>
    </div>
    <div class="abs about-tab">About Us</div>
    <p class="abs disorders">
      Obsessive Compulsive Disorder ✦ Trichotillomania Excoriation Disorder ✦ Generalized Anxiety Disorder ✦<br>
      Panic Disorder ✦ Specific Phobias ✦ Hoarding Disorder ✦ Body Dysmorphic Disorder ✦<br>
      Tic Disorders ✦ ADHD Learning Disorders ✦ Insomnia ✦ Social Anxiety Disorder
    </p>
  </section>

  <section class="treatments-section">
    <div class="abs photo-sunset" role="img" aria-label="Photo of a family seen from behind in a golden field at sunset, a child riding on a parent's shoulders"></div>
    <p class="abs cbt-note">BWC clinicians are highly trained in<br><strong>Cognitive Behavioral Therapy (CBT)</strong> which includes<br>scientifically informed techniques that are tailored<br>to each client’s unique needs.</p>
    <div class="abs treatments"></div>
    <h2 class="abs treatments-title">Treatments We Provide</h2>
    <ul class="abs treatment-list">
      <li>Cognitive Behavioral Therapy (CBT)</li>
      <li>Exposure &amp; Response Prevention (E/RP)</li>
      <li>Comprehensive Behavioral (ComB)</li>
      <li>Habit Reversal Training (HRT)</li>
      <li>Cognitive Behavioral Intervention for Tics (CBIT)</li>
      <li>Acceptance &amp; Commitment Therapy (ACT)</li>
      <li>Organizational Skills Training (OST)</li>
      <li>CBT for Insomnia (CBT-I)</li>
    </ul>
    <svg class="abs footer-curve" viewBox="0 0 792 110" preserveAspectRatio="none"><path d="M0 22 Q 260 58 792 20 L792 110 L0 110 Z" fill="var(--mist)"/></svg>
    <div class="abs director">
      <p class="director-name">Elena R. Marsh, PsyD<br>Executive Director Licensed Clinical Psychologist</p>
      <p class="director-lic">New Jersey Lic. No. 00S00012345 - Pennsylvania Lic. No. PS0000000</p>
    </div>
  </section>

  <footer>
    <div class="abs social" aria-label="Social media links">
      <span style="--c: var(--olive)"></span>
      <span style="--c: #e5b84e"></span>
      <span style="--c: var(--rust)"></span>
    </div>
    <p class="abs website">www.BayfieldWellnessClinic.com</p>
  </footer>
</main>
</body>
</html>
```